Quorvantelline.com

I need a site that I can sell dewatering equipment to the construction industry.
Ie, pipes fittings pumps and other such things needed to remove the groundwater on construction sites. Here in Florida, it’s needed almost everywhere seeing we are at sea level.
I want to be able to sell these products on the site and receive

Coded - Design and coding required

1 page

```html
<!DOCTYPE html>
<html lang="en">
<head>
<meta charset="utf-8">
<title>Quorvantelline LLC – Dewatering Equipment</title>
<link href="https://fonts.googleapis.com/css2?family=Open+Sans:wght@400;600;700;800&display=swap" rel="stylesheet">
<style>
:root{
  --black:#0b0b0b;
  --navy:#143a8a;
  --red:#d7141e;
  --red-dark:#b50d16;
  --blue:#1557b0;
  --card:#e8e8e8;
  --text:#222;
  --muted:#666;
  --grey-band:#efefef;
  --footer:#2e2e2e;
  --footer-bottom:#262626;
  --field:#3b3b3b;
}
*{margin:0;padding:0;box-sizing:border-box}
html,body{width:1200px;height:2384px;overflow:hidden}
body{position:relative;font-family:"Open Sans",Arial,sans-serif;color:var(--text);background:#fff}
.abs{position:absolute}

.topnav{left:0;top:0;width:1200px;height:54px;background:var(--black)}
.topnav ul{list-style:none;position:absolute;left:160px;top:0;height:54px;display:flex;align-items:center;gap:41px}
.topnav li{color:#fff;font-size:10px;font-weight:700;letter-spacing:.2px;text-transform:uppercase}
.nav-icons{right:215px;top:15px;display:flex;gap:28px}

.header{left:0;top:54px;width:1200px;height:73px;background:#fff}
.brand{left:160px;top:20px;font-size:25px;font-weight:800;color:var(--navy);letter-spacing:.3px}
.social{right:212px;top:31px;display:flex;gap:24px}
.social span{width:9px;height:9px;border-radius:50%;background:#111;display:block}

.hero{left:0;top:127px;width:1200px;height:424px;background:linear-gradient(120deg,#8d96a0 0%,#5f6d7c 35%,#3d5d86 55%,#6e7680 75%,#9c9a8e 100%)}

.card{width:210px;height:197px;background:var(--card)}
.card .photo{position:absolute;left:0;top:0;width:210px;height:157px}
.card .label{position:absolute;left:12px;top:168px;font-size:10.5px;font-weight:700;color:#222;text-transform:uppercase}
.featured{left:383px;top:396px;width:210px;height:273px;background:var(--card);box-shadow:0 4px 14px rgba(0,0,0,.25)}
.featured .photo{position:absolute;left:0;top:0;width:210px;height:157px;background:linear-gradient(160deg,#dcdcdc,#a9b4c4)}
.featured .bar{position:absolute;left:0;top:157px;width:210px;height:38px;background:var(--blue);color:#fff;font-size:10.5px;font-weight:700;padding:13px 14px;text-transform:uppercase}
.featured .desc{position:absolute;left:14px;top:205px;font-size:9.5px;color:#777;line-height:15px;text-transform:uppercase}
.featured .cart{position:absolute;left:14px;top:247px;font-size:9.5px;font-weight:700;text-transform:uppercase}
.featured .price{position:absolute;right:14px;top:245px;font-size:12px;font-weight:700}

.promo{left:0;top:966px;width:1200px;height:350px;background:linear-gradient(170deg,#e01a22 0%,#d0121b 55%,#b80d15 100%)}
.promo h2{position:absolute;top:38px;width:1200px;text-align:center;color:#fff;font-size:21px;font-weight:700;letter-spacing:.5px}
.bubble{width:100px;height:100px;border-radius:50%;border:4px solid #e65a60;box-shadow:0 3px 8px rgba(0,0,0,.3)}
.feature{width:377px;height:89px;background:#f5cfd1;text-align:center;padding-top:15px}
.feature h3{font-size:11px;font-weight:700;color:var(--red);margin-bottom:5px}
.feature p{font-size:10.5px;line-height:16px;color:#333;padding:0 28px}

.section-title{width:1200px;text-align:center;font-size:20px;font-weight:600;color:#222}
.tile-back{width:172px;height:143px;background:#e6e6e6}
.tile-photo{width:172px;height:143px}
.tile-label{font-size:14px;color:#555}

.blogs{left:0;top:1667px;width:1200px;height:240px;background:var(--grey-band)}
.blogs .date{position:absolute;top:92px;width:1200px;text-align:center;font-size:10px;font-weight:700}
.blogs p{position:absolute;left:270px;top:111px;width:660px;text-align:center;font-size:11.5px;line-height:19px;color:#333}
.blogs .more{position:absolute;top:182px;width:1200px;text-align:center;font-size:11px;font-weight:700}
.arrow{width:29px;height:46px;background:#d5d5d5;display:flex;align-items:center;justify-content:center}

.subscribe{left:0;top:1907px;width:1200px;height:203px;background:linear-gradient(180deg,#6a6258 0%,#4f4a46 50%,#6d6359 100%)}
.subscribe h2{position:absolute;top:42px;width:1200px;text-align:center;color:#fff;font-size:25px;font-weight:600}
.subscribe .lede{position:absolute;top:84px;width:1200px;text-align:center;color:#eee;font-size:12px}
.email{left:364px;top:117px;width:343px;height:35px;background:#fff;font-size:10px;color:#aaa;padding:11px 14px}
.sub-btn{left:715px;top:117px;width:119px;height:35px;background:var(--red);color:#fff;font-size:12px;font-weight:700;text-align:center;line-height:35px}

.footer{left:0;top:2110px;width:1200px;height:229px;background:var(--footer)}
.field{background:var(--field);font-size:9.5px;color:#888;padding:10px 17px}
.submit{left:160px;top:158px;width:99px;height:34px;background:var(--red);color:#fff;font-size:12px;font-weight:700;text-align:center;line-height:34px;border:1px solid #fff}
.footer h4{font-size:12px;font-weight:700;color:#fff;text-transform:uppercase}
.footer ul{list-style:none}
.footer li{font-size:10px;color:#bbb;line-height:16.5px}
.contact-row{display:flex;gap:14px;font-size:9.5px;color:#bbb;line-height:14px}
.bottom{left:0;top:2339px;width:1200px;height:45px;background:var(--footer-bottom)}
.bottom .copy{position:absolute;left:160px;top:15px;font-size:10px;color:#888}
.bottom .social{top:18px;right:205px;gap:26px}
.bottom .social span{background:#ddd;width:11px;height:11px}
</style>
</head>
<body>

<nav class="abs topnav">
  <ul>
    <li>Dewatering</li><li>Pumps &amp; Equipment</li><li>Groundwater Control Blog</li><li>Support</li><li>About</li>
  </ul>
  <div class="abs nav-icons">
    <svg width="20" height="22" viewBox="0 0 20 22"><rect x="3" y="6" width="12" height="14" fill="none" stroke="#fff" stroke-width="2"/><path d="M6 6V4a3 3 0 0 1 6 0v2" fill="none" stroke="#fff" stroke-width="2"/><circle cx="15" cy="17" r="4" fill="#fff"/></svg>
    <svg width="22" height="22" viewBox="0 0 22 22"><circle cx="9" cy="9" r="6.5" fill="none" stroke="#fff" stroke-width="2.5"/><path d="M14 14l6 6" stroke="#fff" stroke-width="3"/></svg>
  </div>
</nav>

<header class="abs header">
  <div class="abs brand">QUORVANTELLINE LLC</div>
  <div class="abs social"><span></span><span></span><span></span><span></span></div>
</header>

<div class="abs hero" role="img" aria-label="Industrial pump room with blue electric motors and pipework"></div>

<div class="abs card" style="left:160px;top:472px"><div class="photo" role="img" aria-label="Wellpoint swing hose on concrete" style="background:linear-gradient(135deg,#8f8c86,#b3afa8)"></div><div class="label">Wellpoint Standard Swing</div></div>
<div class="abs featured">
  <div class="photo" role="img" aria-label="Blue-tipped wellpoint"></div>
  <div class="bar">Halvorsen MFG - Wellpoint</div>
  <div class="desc">Wellpoint - Jetpoint -20 each-<br>1 1/2" X 3' - Self Jet -Dewater-</div>
  <div class="cart">Add to cart</div>
  <div class="price">$45</div>
</div>
<div class="abs card" style="left:606px;top:472px"><div class="photo" role="img" aria-label="Black siphon well adapter" style="background:linear-gradient(160deg,#e8e8e8,#9a9a9a)"></div><div class="label">Siphon Well Adapter</div></div>
<div class="abs card" style="left:829px;top:472px"><div class="photo" role="img" aria-label="Yellow PVC header pipe plug" style="background:linear-gradient(180deg,#1a1a1a,#3a3000)"></div><div class="label">PVC Header Pipe Plug</div></div>

<div class="abs card" style="left:160px;top:701px"><div class="photo" role="img" aria-label="Wellpoint swing fitting" style="background:linear-gradient(135deg,#a9a59e,#7a766f)"></div><div class="label">Wellpoint Standard Swing</div></div>
<div class="abs card" style="left:383px;top:701px"><div class="photo" role="img" aria-label="Bronze siphon well adapter" style="background:linear-gradient(160deg,#d8d8d8,#a29a8c)"></div><div class="label">Siphon Well Adapter</div></div>
<div class="abs card" style="left:606px;top:701px"><div class="photo" role="img" aria-label="White ball valve with red handle" style="background:linear-gradient(160deg,#f2f2f2,#c9c9c9)"></div><div class="label">Siphon Well Adapter</div></div>
<div class="abs card" style="left:829px;top:701px"><div class="photo" role="img" aria-label="Clear pipe plug with blue tip" style="background:linear-gradient(160deg,#f0f0f0,#d4dbe4)"></div><div class="label">PVC Header Pipe Plug</div></div>

<section class="abs promo">
  <h2>QUORVANTELLINE LLC</h2>
  <div class="abs bubble" role="img" aria-label="Pipe fitting on concrete" style="left:346px;top:93px;background:linear-gradient(135deg,#9b9690,#c7c2ba)"></div>
  <div class="abs bubble" role="img" aria-label="Submersible pump at a site" style="left:750px;top:93px;background:linear-gradient(135deg,#7f95a6,#c2cdd4)"></div>
  <div class="abs feature" style="left:208px;top:213px"><h3>Pipes Fittings Pumps</h3><p>Lorem ipsum dolor sit amet, consectetur adipiscing elit, sed do eiusmod tempor incididunt ut labore et dolore magna</p></div>
  <div class="abs feature" style="left:613px;top:213px"><h3>Remove The Groundwater On Construction Sites</h3><p>Lorem ipsum dolor sit amet, consectetur adipiscing elit, sed do eiusmod tempor incididunt ut labore et dolore magna</p></div>
</section>

<h2 class="abs section-title" style="left:0;top:1378px">Pump &amp; Equipments</h2>
<div class="abs tile-back" style="left:224px;top:1470px"></div>
<div class="abs tile-back" style="left:427px;top:1470px"></div>
<div class="abs tile-back" style="left:630px;top:1470px"></div>
<div class="abs tile-back" style="left:834px;top:1470px"></div>
<div class="abs tile-photo" role="img" aria-label="Submersible pump in water" style="left:207px;top:1438px;background:linear-gradient(160deg,#8fb3c6,#5a7c8c)"></div>
<div class="abs tile-photo" role="img" aria-label="Pump manufacturing floor" style="left:410px;top:1438px;background:linear-gradient(160deg,#c9ccd1,#5d6b7c)"></div>
<div class="abs tile-photo" role="img" aria-label="Installed blue pumps" style="left:613px;top:1438px;background:linear-gradient(160deg,#b6bcc6,#3d4ea3)"></div>
<div class="abs tile-photo" role="img" aria-label="Pump room project" style="left:817px;top:1438px;background:linear-gradient(160deg,#dcdfe2,#8d96a0)"></div>
<div class="abs tile-label" style="left:245px;top:1587px">Pumps</div>
<div class="abs tile-label" style="left:446px;top:1587px">Manufacturing</div>
<div class="abs tile-label" style="left:646px;top:1587px">Installations</div>
<div class="abs tile-label" style="left:851px;top:1587px">Projects</div>

<section class="abs blogs">
  <h2 class="abs section-title" style="top:42px">Our Blogs</h2>
  <div class="date">11 Jun-2018</div>
  <p>Lorem ipsum dolor sit amet, consectetur adipiscing elit, sed do eiusmod tempor incididunt ut labore et dolore magna aliqua. Ut enim ad minim veniam, quis nostrud exercitation ullamco laboris nisi ut aliquip ex ea commodo consequat. Duis aute irure dolor in reprehenderit in voluptate velit esse cillum dolore eu fugiat nulla pariatur.</p>
  <div class="more">Learn More</div>
  <div class="abs arrow" style="left:187px;top:87px"><svg width="10" height="16"><path d="M8 2L2 8l6 6" fill="none" stroke="#fff" stroke-width="2"/></svg></div>
  <div class="abs arrow" style="left:982px;top:87px"><svg width="10" height="16"><path d="M2 2l6 6-6 6" fill="none" stroke="#fff" stroke-width="2"/></svg></div>
</section>

<section class="abs subscribe" role="img" aria-label="Pump station with large orange pipes in the background">
  <h2>Subscribe Quorvantelline LLC</h2>
  <div class="lede">Sign up for our newsletter and be the first to learn about new Quorvantelline LLC</div>
  <div class="abs email">Enter Email Address</div>
  <div class="abs sub-btn">Subscribe</div>
</section>

<footer class="abs footer">
  <div class="abs field" style="left:160px;top:48px;width:168px;height:35px">Name</div>
  <div class="abs field" style="left:332px;top:48px;width:170px;height:35px">Email</div>
  <div class="abs field" style="left:160px;top:88px;width:342px;height:62px">Message</div>
  <div class="abs submit">Submit</div>

  <h4 class="abs" style="left:583px;top:45px">Navigation</h4>
  <ul class="abs" style="left:583px;top:66px">
    <li>- Dewatering</li><li>- Pumps &amp; Equipment</li><li>- Groundwater Control Blog</li><li>- Support</li><li>- About</li><li>- Contact Us</li>
  </ul>

  <h4 class="abs" style="left:847px;top:45px">Contact Us</h4>
  <div class="abs contact-row" style="left:849px;top:70px">
    <svg width="12" height="16" viewBox="0 0 12 16"><path d="M6 0a6 6 0 0 1 6 6c0 4-6 10-6 10S0 10 0 6a6 6 0 0 1 6-6z" fill="#ddd"/><circle cx="6" cy="6" r="2.2" fill="#2e2e2e"/></svg>
    <span>Lorem Ipsum Dlor Sit Amet<br>Consectetor Dolor Sit Amet<br>Dolor Sit</span>
  </div>
  <div class="abs contact-row" style="left:849px;top:132px">
    <svg width="12" height="12" viewBox="0 0 12 12"><path d="M2 1l2.5 0 1 3-1.5 1a6 6 0 0 0 3 3l1-1.5 3 1V10a1.5 1.5 0 0 1-1.5 1.5C4.5 11.5.5 7.5.5 2.5A1.5 1.5 0 0 1 2 1z" fill="#ddd"/></svg>
    <span>+00 1234 456789</span>
  </div>
  <div class="abs contact-row" style="left:849px;top:158px">
    <svg width="13" height="10" viewBox="0 0 13 10"><rect x=".5" y=".5" width="12" height="9" fill="none" stroke="#ddd"/><path d="M.5.5l6 5 6-5" fill="none" stroke="#ddd"/></svg>
    <span>info@quorvantelline.com</span>
  </div>
</footer>

<div class="abs bottom">
  <div class="copy">© 2018 Quorvantelline llc. All rights reserved.</div>
  <div class="abs social"><span></span><span></span><span></span><span></span></div>
</div>

</body>
</html>
```